New funky, super creative logo design for printing business

Stamp, Wrap and Ship

We are a new digital printing business, based on the Gold Coast of Australia. We have a web site under construction - www.stampwrapandship.net, which will aim at the Business to Business market. We are digital printers, offering a wide variety of print products from business cards to wide format print jobs for consumers and small to medium sized business'. We offer up to date technological, digital and wide format print, at hi octane speed. Our prices are very competitive, and turnaround is super fast.

We like to think outside the box, and this should shine through in the design and colours that you use. Be bold and creative, we want to stand out from the crowd.

We will also soon be needing a full suite of marketing collaterals - posters, letterheads, scrap pads, calendars, banners etc. but this will come later, once we have decided on the logo and layouts.

We want a vibrant, bold image, communicating vibrancy and excitement.

Details on the card are company name: Stamp, Wrap and Ship.
www.stampwrapandship.net.
contact: Marisol (+61)437281956
e-mail:marisol@stampwrapandship.net

I must be able to change some of the details such as the name and number on the card.

Target Market(s)

Business to business, small retail, some individuals

Industry/Entity Type

Construction

Requirements
Must have
• Unique funky logo.
Nice to have
• A three dimensional look,with depth in the logo.

```html
<!DOCTYPE html>
<html lang="en">
<head>
<meta charset="utf-8">
<title>Stamp, Wrap and Ship — Business Cards</title>
<link rel="stylesheet" href="https://fonts.googleapis.com/css2?family=Michroma&display=swap">
<style>
  :root {
    --backdrop: #3b3b3b;
    --card-light: #ffffff;
    --card-edge: #d9d9d9;
    --ink: #0a0a0a;
    --accent-cyan: #55c6ea;
  }
  * { margin: 0; padding: 0; box-sizing: border-box; }
  html, body {
    width: 1200px;
    height: 534px;
    overflow: hidden;
    background: var(--backdrop);
  }
  .stage {
    position: relative;
    width: 1200px;
    height: 534px;
  }
  .card {
    position: absolute;
    top: 119px;
    width: 517px;
    height: 294px;
    background: radial-gradient(ellipse at 50% 42%, var(--card-light) 0%, #f2f2f2 50%, var(--card-edge) 100%);
    font-family: "Michroma", sans-serif;
    color: var(--ink);
    overflow: hidden;
  }
  .card--square { left: 62px; }
  .card--rounded { left: 622px; border-radius: 17px; }

  .brand__square {
    position: absolute;
    left: 150px;
    top: 36px;
    width: 100px;
    height: 100px;
    background: var(--accent-cyan);
  }
  .brand__name {
    position: absolute;
    left: 124px;
    top: 142px;
    width: 286px;
    font-size: 25px;
    line-height: 1.08;
    font-weight: 400;
    text-transform: uppercase;
    color: var(--ink);
    white-space: nowrap;
  }
  .brand__name span { display: block; }
  .brand__line2 { text-align: right; }

  .contact {
    position: absolute;
    left: 0;
    right: 0;
    top: 246px;
    text-align: center;
    font-size: 8.2px;
    letter-spacing: 0.01em;
    text-transform: uppercase;
    white-space: nowrap;
    color: var(--ink);
  }
  .contact__divider { margin: 0 7px; }
  .website {
    position: absolute;
    left: 0;
    right: 0;
    top: 263px;
    text-align: center;
    font-size: 11px;
    letter-spacing: 0.04em;
    text-transform: uppercase;
    white-space: nowrap;
    color: var(--ink);
  }
</style>
</head>
<body>
<main class="stage">
  <article class="card card--square">
    <div class="brand__square"></div>
    <h1 class="brand__name"><span>Stamp, Wrap</span><span class="brand__line2">and Ship</span></h1>
    <p class="contact">Phone: Marisol (+61)437281956<span class="contact__divider">//</span>E-mail:marisol@stampwrapandship.net</p>
    <p class="website">www.stampwrapandship.net</p>
  </article>

  <article class="card card--rounded">
    <div class="brand__square"></div>
    <h1 class="brand__name"><span>Stamp, Wrap</span><span class="brand__line2">and Ship</span></h1>
    <p class="contact">Phone: Marisol (+61)437281956<span class="contact__divider">//</span>E-mail:marisol@stampwrapandship.net</p>
    <p class="website">www.stampwrapandship.net</p>
  </article>
</main>
</body>
</html>
```